Website for Hash Orbita a cyrpto Mining company that sells crypto mining rigs

β€œIn the age of de-centralised financial services, individuals with a relatively small investment can use their own hardware to process crypto transactions and earn a substantial second income.”

Hash Orbita provide a personal home and hosted mining solutions to enable individuals to earn monthly crypto currencies of today and the future.”
Home/Products/About
Images – I had assumed this was part of the Design? For the home page I have a 10 second video of blockchain. I can only find on Pixelvault For any text or sections please refer to our old website www.thirdheron.ae
https://www.pixelvaultmedia.com/video/clip-2947163058-block-chain-concept---consists-network-connections I can buy and send?
On each page I will have a video similar, can you just put placeholder images and videos. I can replace. I am pretty good with Wordpress.
Updates

Please use text from my old website www.thirdheronmining.com

Target Market(s)

High Net wealth interested in Crypto

Industry/Entity Type

Crypto Mining

Coding

Coded - Design and coding required

Number of Pages Required

5+ page

Font styles to use
Other font styles liked:
• Sansation

Colors
0054AA
0677BA
7BADD7
CADEEF
E8F1F8

Requirements
Must have
• Video as banner (Will supply Video), Wordpress
Nice to have
• Will need Member login and Shop in future, please ensure this will be possible. (But not part of this project)

```html
<!DOCTYPE html>
<html lang="en">
<head>
<meta charset="utf-8">
<title>Hash Orbita – Crypto Mining Rigs</title>
<link rel="stylesheet" href="https://fonts.googleapis.com/css2?family=Roboto:ital,wght@0,400;0,500;0,700;1,400&display=swap">
<style>
:root{
  --navy:#15174a;
  --navy-deep:#0c0e2e;
  --blue:#0677BA;
  --blue-dark:#0054AA;
  --blue-bright:#0a9be6;
  --cyan:#00c6f0;
  --ink:#222;
  --muted:#666;
  --grey-band:#f3f3f3;
  --white:#fff;
  --black:#000;
}
*{margin:0;padding:0;box-sizing:border-box}
html,body{width:1200px;height:4886px;overflow:hidden}
body{position:relative;font-family:"Roboto",Arial,sans-serif;color:var(--ink);background:var(--white)}
.abs{position:absolute}
.btn{position:absolute;display:flex;align-items:center;justify-content:center;border-radius:24px;font-weight:700;font-size:13px;text-transform:uppercase;color:var(--white);background:linear-gradient(90deg,var(--blue-dark),var(--blue-bright));}

/* hero */
.hero{position:absolute;left:0;top:0;width:1200px;height:710px;background:radial-gradient(ellipse at 50% 45%,#1d2a7a 0%,var(--navy) 45%,var(--navy-deep) 100%);overflow:hidden}
.hero-media{position:absolute;left:0;top:170px;width:1200px;height:420px;background:radial-gradient(ellipse at 50% 45%,rgba(40,170,255,.75) 0%,rgba(20,110,230,.45) 35%,rgba(20,40,120,0) 70%)}
.brand{position:absolute;left:74px;top:100px;width:240px;font-size:24px;font-weight:500;letter-spacing:1px;color:var(--blue-bright);text-align:center;white-space:nowrap}
.brand-dot{position:absolute;left:162px;top:16px;width:62px;height:62px;border-radius:50%;border:4px solid var(--blue-bright)}
.nav{position:absolute;top:51px;display:flex;gap:44px;left:650px;font-size:13px;font-weight:700;color:var(--white)}
.nav .active{color:var(--blue-bright)}
.hero-title{position:absolute;left:0;top:314px;width:1200px;text-align:center;font-size:50px;line-height:52px;font-weight:700;color:var(--white);text-shadow:0 2px 10px rgba(0,0,0,.55);text-transform:uppercase}
.btn-light{position:absolute;left:531px;top:436px;width:136px;height:47px;border-radius:24px;background:var(--white);color:var(--blue);font-size:12px;font-weight:700;display:flex;align-items:center;justify-content:center}
.dots{position:absolute;left:578px;top:596px;display:flex;gap:5px}
.dots i{width:13px;height:13px;border-radius:50%;background:var(--white)}

.h2{position:absolute;left:0;width:1200px;text-align:center;font-size:37px;font-weight:700;color:#111;text-transform:uppercase}

/* services */
.card{position:absolute;width:309px;height:376px;background:var(--white);box-shadow:0 0 24px rgba(10,140,230,.18);text-align:center}
.card svg.icon{position:absolute;left:99px;top:44px}
.card h3{position:absolute;left:0;top:166px;width:100%;font-size:21px;font-weight:700;color:#111}
.card p{position:absolute;left:38px;top:210px;width:233px;font-size:13px;line-height:22px;color:var(--muted)}
.card .more{position:absolute;left:143px;top:318px}

/* about */
.about{position:absolute;left:0;top:1864px;width:1200px;height:421px;background:var(--grey-band)}
.about-mark{position:absolute;left:246px;top:84px;width:220px;height:220px;border-radius:50%;border:14px solid var(--blue-bright);display:flex;align-items:center;justify-content:center;font-size:28px;font-weight:700;color:var(--blue-bright);text-align:center;line-height:34px}
.about h2{position:absolute;left:599px;top:90px;font-size:35px;font-weight:700;color:#111;text-transform:uppercase;white-space:nowrap}
.about .lead{position:absolute;left:599px;top:146px;width:470px;font-size:19px;line-height:22px;color:var(--blue-bright)}
.about .body{position:absolute;left:599px;top:204px;width:480px;font-size:13px;line-height:22px;color:var(--muted)}

/* team */
.member{position:absolute;top:2448px;width:256px;text-align:center}
.member .photo{width:256px;height:294px}
.member h3{margin:24px -30px 0;font-size:21px;font-weight:700;color:#111;text-transform:uppercase;white-space:nowrap}
.member p{margin:16px auto 0;width:250px;font-size:13px;line-height:22px;color:var(--muted)}

/* testimonials */
.testimonials{position:absolute;left:0;top:2999px;width:1200px;height:503px;background:linear-gradient(110deg,#0a55c9 0%,#0a7fe0 55%,var(--cyan) 100%)}
.testimonials h2{position:absolute;left:0;top:92px;width:1200px;text-align:center;font-size:35px;font-weight:700;color:var(--white)}
.quote{position:absolute;top:152px;height:245px;background:var(--white);padding:20px 24px}
.quote p{font-size:12.5px;line-height:22px;font-style:italic;color:var(--muted)}
.quote strong{display:block;margin-top:14px;font-size:15.5px;line-height:22px;color:#111;font-weight:500}

/* faq */
.faq-sub{position:absolute;left:0;top:3647px;width:1200px;text-align:center;font-size:13px;color:var(--muted)}
.faq-item{position:absolute;left:271px;width:658px;height:58px;background:var(--white);box-shadow:0 2px 10px rgba(0,0,0,.12);padding-left:32px;display:flex;align-items:center;font-size:14px;font-weight:500;color:#444}

/* footer */
.footer{position:absolute;left:0;top:4180px;width:1200px;height:706px}
.footer h4{position:absolute;top:246px;font-size:25px;font-weight:700;color:var(--white);text-transform:uppercase}
.footer .rule{position:absolute;top:296px;width:66px;height:3px;background:var(--blue-bright)}
.field{position:absolute;border:1px solid #bbb;font-size:11px;color:var(--white);padding-left:18px;display:flex;align-items:center}
.field.msg{align-items:flex-start;padding-top:10px}
.submit{position:absolute;left:106px;top:526px;width:190px;height:38px;background:var(--blue-bright);color:var(--white);font-size:14px;font-weight:700;display:flex;align-items:center;justify-content:center}
.contact-row{position:absolute;left:580px;display:flex;gap:18px;color:var(--white);font-size:14px;line-height:21px}
.contact-row .ico{width:34px;height:34px;flex:none;border:1.5px solid var(--white);border-radius:50%;display:flex;align-items:center;justify-content:center}
.links{position:absolute;left:904px;top:336px;list-style:none;color:var(--white);font-size:14px;line-height:30px}
.divider{position:absolute;left:106px;top:606px;width:982px;height:1px;background:#333}
.copy{position:absolute;left:110px;top:646px;font-size:13px;color:var(--white)}
.social{position:absolute;top:636px;width:35px;height:35px;border:2px solid var(--white);border-radius:50%}
</style>
</head>
<body>

<header class="hero">
  <div class="hero-media" role="img" aria-label="Banner video placeholder: glowing blue blockchain cube and chain links"></div>
  <div class="brand-dot"></div>
  <div class="brand">HASH ORBITA</div>
  <nav class="nav"><span class="active">HOME</span><span>PRODUCTS</span><span>ABOUT</span></nav>
  <a class="btn" style="left:948px;top:36px;width:140px;height:47px;font-size:12px">Get a quote</a>
  <h1 class="hero-title">Crypto Mining Company<br>That Sells Crypto Mining Rigs</h1>
  <a class="btn-light">GET STARTED</a>
  <div class="dots"><i></i><i></i><i></i></div>
  <svg class="abs" style="left:0;top:600px" width="1200" height="110" viewBox="0 0 1200 110">
    <path d="M0 95 C260 40 430 40 640 75 C860 110 1040 80 1200 20 L1200 110 L0 110Z" fill="var(--blue-bright)"/>
    <path d="M0 105 C260 55 430 55 640 88 C860 120 1040 95 1200 38 L1200 110 L0 110Z" fill="var(--white)"/>
  </svg>
</header>

<h2 class="h2" style="top:818px">Our Services</h2>

<svg width="0" height="0" style="position:absolute">
  <defs>
    <symbol id="frame" viewBox="0 0 110 100"><rect x="3" y="3" width="104" height="94" rx="8" fill="none" stroke="var(--blue-bright)" stroke-width="5"/></symbol>
    <symbol id="more" viewBox="0 0 24 24"><circle cx="12" cy="12" r="11" fill="var(--blue-bright)"/><path d="M7 10l5 5 5-5" fill="none" stroke="#fff" stroke-width="2.5"/></symbol>
  </defs>
</svg>

<div class="card" style="left:112px;top:904px">
  <svg class="icon" width="110" height="100" viewBox="0 0 110 100"><use href="#frame"/><rect x="28" y="30" width="22" height="42" fill="var(--blue)"/><rect x="48" y="34" width="36" height="26" fill="none" stroke="var(--blue)" stroke-width="5"/><rect x="60" y="62" width="12" height="8" fill="var(--blue)"/></svg>
  <h3>Hardware Installation</h3>
  <p>In the last few years, the technology required to 'mine' crypto has fallen significantly and the speed and ability has increased.</p>
  <svg class="more" width="24" height="24"><use href="#more"/></svg>
</div>
<div class="card" style="left:446px;top:904px">
  <svg class="icon" width="110" height="100" viewBox="0 0 110 100"><use href="#frame"/><path d="M30 78 L66 36" stroke="var(--blue)" stroke-width="7"/><path d="M48 24 Q72 20 86 40" fill="none" stroke="var(--blue)" stroke-width="7"/><circle cx="72" cy="68" r="10" fill="var(--blue)"/></svg>
  <h3>Currency Mining</h3>
  <p>Our typical "Opal" rig contains 6 high powered gaming cards (GPUs) that produce amazing processing capability.</p>
  <svg class="more" width="24" height="24"><use href="#more"/></svg>
</div>
<div class="card" style="left:779px;top:904px">
  <svg class="icon" width="110" height="100" viewBox="0 0 110 100"><use href="#frame"/><rect x="36" y="30" width="38" height="38" rx="4" fill="none" stroke="var(--blue)" stroke-width="5"/><rect x="46" y="40" width="18" height="18" fill="var(--blue)"/><path d="M44 22v8M55 22v8M66 22v8M44 68v8M55 68v8M66 68v8M28 40h8M28 58h8M74 40h8M74 58h8" stroke="var(--blue)" stroke-width="3"/></svg>
  <h3>Crypto Earnings</h3>
  <p>With 50,000 AED invested, the Third Heron mining rig returns up to 0.4 ETH per month. So if you buy ETH today you could buy 5</p>
  <svg class="more" width="24" height="24"><use href="#more"/></svg>
</div>
<div class="card" style="left:112px;top:1308px">
  <svg class="icon" width="110" height="100" viewBox="0 0 110 100"><use href="#frame"/><rect x="34" y="40" width="30" height="32" rx="4" fill="var(--blue)"/><path d="M40 40v-8a9 9 0 0 1 18 0v8" fill="none" stroke="var(--blue)" stroke-width="5"/><path d="M64 48h16M64 58h20M64 68h14" stroke="var(--blue)" stroke-width="3"/></svg>
  <h3>Earn Crypto Every Month</h3>
  <p>When you become a Third Heron mining member, we help you open a CoinHarbor or Ledgerly Crypto account for free.</p>
  <svg class="more" width="24" height="24"><use href="#more"/></svg>
</div>
<div class="card" style="left:446px;top:1308px">
  <svg class="icon" width="110" height="100" viewBox="0 0 110 100"><use href="#frame"/><circle cx="55" cy="50" r="20" fill="none" stroke="var(--blue)" stroke-width="10" stroke-dasharray="9 5"/><circle cx="55" cy="50" r="12" fill="none" stroke="var(--blue)" stroke-width="4"/><path d="M49 56l12-12" stroke="var(--blue)" stroke-width="3"/></svg>
  <h3>Service &amp; Maintenance</h3>
  <p>The Third Heron service and maintenance team guarantee 96% platform up time, 24/7 customer service and same day call</p>
  <svg class="more" width="24" height="24"><use href="#more"/></svg>
</div>
<div class="card" style="left:779px;top:1308px">
  <svg class="icon" width="110" height="100" viewBox="0 0 110 100"><use href="#frame"/><path d="M55 78V30M55 24l-9 10h18zM55 52H30M24 52l10-8v16zM55 52h25M86 52l-10-8v16z" stroke="var(--blue)" stroke-width="5" fill="var(--blue)"/></svg>
  <h3>Flexible Mining</h3>
  <p>Our Rig design means that you can choose to mine any cryptocurrency, not just Ethereum. Depending on your risk profile, you</p>
  <svg class="more" width="24" height="24"><use href="#more"/></svg>
</div>

<a class="btn" style="left:504px;top:1714px;width:192px;height:47px;font-size:12px">Contact us today</a>

<section class="about">
  <div class="about-mark">HASH<br>ORBITA</div>
  <h2>About Hash Orbita</h2>
  <p class="lead">IT and Operations since 2000, Digital Payments since 2007, Crypto since 2012.</p>
  <p class="body">Martin and Ilian were part of the core team that built Paywendo.com. Nolan has been running IT and Operation teams of large companies for many years before setting up his own IT and Security Consultancy. Together this team know how to build, run and scale technology in Crypto and Payments, we only make 10% of your profits so we're dedicated to make your Third Heron mining rigs perform.</p>
</section>

<h2 class="h2" style="top:2376px">Our Team</h2>
<div class="member" style="left:146px">
  <div class="photo" role="img" aria-label="Portrait photo of co-founder Martin Fairley" style="background:linear-gradient(160deg,#8a7a70,#3b3330)"></div>
  <h3>Martin Fairley</h3>
  <p>Co-Founder who operates the business licenses, accounts and financial service partnerships.</p>
</div>
<div class="member" style="left:472px">
  <div class="photo" role="img" aria-label="Portrait photo of co-founder Nolan Kerrigan" style="background:linear-gradient(160deg,#f2f2f2,#c9c2bc)"></div>
  <h3>Nolan Kerrigan</h3>
  <p>Co-Founder who designs, builds and maintains our hardware and software solutions.</p>
</div>
<div class="member" style="left:798px">
  <div class="photo" role="img" aria-label="Photo of the technology and operations team" style="background:linear-gradient(100deg,#3c4a5c,#b9c2cc 60%,#7d8a99)"></div>
  <h3>Petar &amp; Ilian Varov</h3>
  <p>Our Technology and Operations gurus who track the crypto markets daily. Their remote access to the Third Heron Mining rigs ensure they are optimised.</p>
</div>

<section class="testimonials">
  <h2>TESTIMONIALS</h2>
  <svg class="abs" style="left:40px;top:258px" width="26" height="50" viewBox="0 0 26 50"><path d="M22 3L4 25l18 22" fill="none" stroke="#fff" stroke-width="3"/></svg>
  <svg class="abs" style="left:1132px;top:258px" width="26" height="50" viewBox="0 0 26 50"><path d="M4 3l18 22L4 47" fill="none" stroke="#fff" stroke-width="3"/></svg>
  <div class="quote" style="left:112px;width:472px">
    <p>"I'd been hearing a few mates on the golf course tell me how they had bought crypto currency a few years ago and now were enjoying the returns, I though I'd missed the boat. Martin explained that now crypto is mainstream, and technology has advanced massively, I didn't need to be a millionaire with a warehouse in Iceland to participate. Since investing in my own mining rig, it sits in my spare room and returns about 4,700 AED each month."</p>
    <strong>Regional Sales &amp; Account Director | Healthcare Systems</strong>
  </div>
  <div class="quote" style="left:614px;width:474px">
    <p>"I had 10 thousands pounds saved but going nowhere. Nolan explained that could buy a mining rig so I decided to invest it in the hardware. He came around himself, took about 2 hours to set it up, showed me how to open a CoinHarbor account and how to check the daily performance on my mobile or laptop. I can't quite believe it's making me money for what looks like nothing."</p>
    <strong>Office Manager | Dubai Business</strong>
  </div>
</section>

<h2 class="h2" style="top:3592px">FAQ</h2>
<p class="faq-sub">Below we've provided some info on home mining, crypto earnings and our current choice to mining ETH.</p>
<div class="faq-item" style="top:3690px">What do I need to support a Home Mining rig?</div>
<div class="faq-item" style="top:3769px">Would you like us to Host your Rig, potentially multiple Rigs in your own dedicated..</div>
<div class="faq-item" style="top:3848px">Isn't Crypto Mining really bad for the planet?</div>
<div class="faq-item" style="top:3927px">EIP 1559?&nbsp; The reduction of gas fees to stay competitive and reduce supply.</div>
<div class="faq-item" style="top:4005px">What is The Flippening?</div>
<div class="faq-item" style="top:4084px">What is the difference between Proof of Work and Proof of Stake?</div>

<footer class="footer">
  <svg class="abs" style="left:0;top:0" width="1200" height="706" viewBox="0 0 1200 706">
    <path d="M0 110 C200 60 420 50 640 100 C860 150 1040 130 1200 50 L1200 706 L0 706Z" fill="var(--blue-bright)"/>
    <path d="M0 122 C200 72 420 62 640 112 C860 162 1040 150 1200 72 L1200 706 L0 706Z" fill="var(--black)"/>
  </svg>
  <h4 style="left:106px">Request a quote</h4><div class="rule" style="left:106px"></div>
  <h4 style="left:580px">Contact us</h4><div class="rule" style="left:580px"></div>
  <h4 style="left:904px">Quick links</h4><div class="rule" style="left:904px"></div>

  <div class="field" style="left:106px;top:338px;width:216px;height:42px">First Name</div>
  <div class="field" style="left:337px;top:338px;width:216px;height:42px">Last Name</div>
  <div class="field" style="left:106px;top:399px;width:216px;height:42px">Phone Number</div>
  <div class="field" style="left:337px;top:399px;width:216px;height:42px">Email Address</div>
  <div class="field msg" style="left:106px;top:458px;width:447px;height:47px">Message</div>
  <div class="submit">SUBMIT</div>

  <div class="contact-row" style="top:332px"><span class="ico"><svg width="16" height="18" viewBox="0 0 16 18"><path d="M8 17s6-6 6-10A6 6 0 0 0 2 7c0 4 6 10 6 10z" fill="none" stroke="#fff" stroke-width="1.6"/><circle cx="8" cy="7" r="2" fill="#fff"/></svg></span><span>Address:<br>Lorem ipsum dolor sit am<br>et, consectetur adip</span></div>
  <div class="contact-row" style="top:424px"><span class="ico"><svg width="16" height="16" viewBox="0 0 16 16"><path d="M3 1l3 3-2 2c1 2 3 4 6 6l2-2 3 3-2 2C7 15 1 9 1 3z" fill="none" stroke="#fff" stroke-width="1.5"/></svg></span><span>Phone:<br>+1 888 888 8888</span></div>
  <div class="contact-row" style="top:492px"><span class="ico"><svg width="16" height="12" viewBox="0 0 16 12"><rect x="1" y="1" width="14" height="10" fill="none" stroke="#fff" stroke-width="1.5"/><path d="M1 1l7 6 7-6" fill="none" stroke="#fff" stroke-width="1.5"/></svg></span><span>Email:<br>info@companyname.com</span></div>

  <ul class="links"><li>Home</li><li>About us</li><li>Events</li><li>Products</li><li>Blog</li><li>Privacy policy</li><li>Contact</li></ul>

  <div class="divider"></div>
  <p class="copy">© Copyright 2021 Comany name. All Rights Reserved.</p>
  <span class="social" style="left:959px" aria-label="Social link"></span>
  <span class="social" style="left:1003px" aria-label="Social link"></span>
  <span class="social" style="left:1049px" aria-label="Social link"></span>
</footer>

</body>
</html>
```